Oil and gas industry project solutions company needs professional cards with Canadian aboriginal fee

We are a aboriginally owned company that is focused on Project Planning, Management, Inspection & Consulting for Canada's Petroleum Industry. We have a logo that we would like to incorporate into a professional looking business card. We are professionals that offer services from project inception to completion.

Target Market(s)

Major industry leaders like NorvaLine, Brisk, Vorkantrel, Pelquist etc.

Industry/Entity Type

Industry

Contact Information for Business Card

Milo Rensford
milo@orvelpike.ca
250 555 0187

Requirements
Must have
• OrvelPike Inc. logo.
• Address is: RR4, Site2, Comp17 Fort St. John, BC V9X 2K3 Traditional Territory of the Treaty 8 People
• Colors that are in logo
• Banner or picture on back
• Ability to put different names and contacts
• Website: orvelpike.ca
• "Project Planning, Management, Inspection & Consulting for Canada's Petroleum Industry"

```html
<!DOCTYPE html>
<html lang="en">
<head>
<meta charset="utf-8">
<title>OrvelPike Inc. Business Card</title>
<link rel="stylesheet" href="https://fonts.googleapis.com/css2?family=Source+Sans+3:wght@400;600;700&display=swap">
<style>
  :root {
    --navy: #2b3174;
    --green: #6ab245;
    --ink: #1e1e24;
    --card: #ffffff;
    --stage: #e8e5e1;
    --rule: #2a2a2a;
    --photo-light: #f1f2f3;
    --photo-mid: #d9dcde;
  }
  * { margin: 0; padding: 0; box-sizing: border-box; }
  html, body { width: 1200px; height: 1000px; overflow: hidden; }
  body {
    background: var(--stage);
    font-family: "Source Sans 3", "Myriad Pro", sans-serif;
    color: var(--ink);
    position: relative;
  }
  .card {
    position: absolute;
    left: 265px;
    width: 665px;
    height: 397px;
    border-radius: 22px;
    background: var(--card);
    overflow: hidden;
    box-shadow: 0 6px 14px rgba(0,0,0,0.18);
  }
  .card--front { top: 73px; }
  .card--back { top: 533px; }

  .brand {
    position: absolute;
    display: flex;
    align-items: center;
    gap: 14px;
  }
  .brand__dot {
    width: 30px; height: 30px;
    border-radius: 50%;
    background: var(--green);
  }
  .brand__name {
    font-weight: 700;
    font-size: 40px;
    color: var(--navy);
    letter-spacing: -0.5px;
    white-space: nowrap;
  }
  .card--front .brand { left: 40px; top: 80px; }

  .services {
    position: absolute;
    left: 36px; top: 170px;
    list-style: none;
    font-size: 17px;
    line-height: 22px;
  }
  .services li { position: relative; padding-left: 17px; }
  .services li::before {
    content: "";
    position: absolute;
    left: 1px; top: 8px;
    width: 7px; height: 7px;
    border-radius: 50%;
    background: var(--green);
  }

  .holder {
    position: absolute;
    right: 32px; top: 232px;
    font-weight: 700;
    font-size: 22px;
    color: var(--navy);
    letter-spacing: 0.3px;
  }
  .divider {
    position: absolute;
    left: 32px; right: 32px; top: 271px;
    height: 1.5px;
    background: var(--rule);
  }
  .address {
    position: absolute;
    left: 32px; top: 301px;
    display: flex;
    gap: 7px;
    font-size: 17px;
    line-height: 22px;
  }
  .address svg { flex: none; margin-top: 3px; }

  .contacts {
    position: absolute;
    right: 29px; top: 297px;
    list-style: none;
    font-size: 17px;
    line-height: 24.5px;
    text-align: right;
  }
  .contacts li { display: flex; justify-content: flex-end; align-items: center; gap: 7px; }
  .contacts svg { flex: none; }

  .backdrop {
    position: absolute;
    inset: 0;
    background: radial-gradient(ellipse at 55% 45%, var(--photo-mid) 0%, var(--photo-light) 70%);
  }
  .card--back .brand {
    left: 0; right: 0; top: 180px;
    justify-content: center;
  }
  .card--back .brand__name { font-size: 44px; }
  .site {
    position: absolute;
    left: 0; right: 0; top: 344px;
    text-align: center;
    font-weight: 600;
    font-size: 18px;
    letter-spacing: 1.6px;
    color: var(--navy);
  }
</style>
</head>
<body>
  <section class="card card--front" aria-label="Card front">
    <div class="brand">
      <span class="brand__dot"></span>
      <span class="brand__name">OrvelPike Inc.</span>
    </div>

    <ul class="services">
      <li>Project Planning</li>
      <li>Management</li>
      <li>Inspection &amp; Consulting for<br>Canada's Petroleum Industry</li>
    </ul>

    <p class="holder">MILO RENSFORD</p>
    <div class="divider"></div>

    <div class="address">
      <svg width="13" height="19" viewBox="0 0 13 19" aria-hidden="true">
        <path d="M6.5 0C2.9 0 0 2.8 0 6.3 0 11 6.5 19 6.5 19S13 11 13 6.3C13 2.8 10.1 0 6.5 0z" fill="var(--navy)"/>
        <circle cx="6.5" cy="6.3" r="2.6" fill="#fff"/>
      </svg>
      <p>RR4, Site2, Comp17 Fort St. John,<br>BC V9X 2K3<br>Traditional Territory of the Treaty 8 People</p>
    </div>

    <ul class="contacts">
      <li>250 555 0187
        <svg width="16" height="12" viewBox="0 0 16 12" aria-hidden="true">
          <path d="M1 4C1 1.5 15 1.5 15 4L12.5 5 11 3.5H5L3.5 5z" fill="var(--navy)"/>
          <rect x="3" y="5.5" width="10" height="6" rx="1" fill="var(--navy)"/>
          <circle cx="8" cy="8.5" r="1.6" fill="#fff"/>
        </svg>
      </li>
      <li>milo@orvelpike.ca
        <svg width="16" height="12" viewBox="0 0 16 12" aria-hidden="true">
          <rect x="0" y="0" width="16" height="12" rx="1" fill="var(--navy)"/>
          <path d="M1 1.5L8 7 15 1.5" fill="none" stroke="#fff" stroke-width="1.3"/>
        </svg>
      </li>
      <li>www.orvelpike.ca
        <svg width="16" height="16" viewBox="0 0 16 16" aria-hidden="true">
          <circle cx="7" cy="7" r="6" fill="none" stroke="var(--navy)" stroke-width="1.6"/>
          <path d="M1 7h12M7 1c-3 3-3 9 0 12M7 1c3 3 3 9 0 12" fill="none" stroke="var(--navy)" stroke-width="1"/>
          <path d="M9 9l6 2.5-2.5 1-1 2.5z" fill="var(--navy)"/>
        </svg>
      </li>
    </ul>
  </section>

  <section class="card card--back" aria-label="Card back">
    <div class="backdrop" role="img" aria-label="Faded photograph of pipeline workers on a snowy construction site"></div>
    <div class="brand">
      <span class="brand__dot"></span>
      <span class="brand__name">OrvelPike Inc.</span>
    </div>
    <p class="site">www.orvelpike.ca</p>
  </section>
</body>
</html>
```